Velno - Website for fruit & juice

- The location of the outlet is Fort Kochi in India.
- Fort Kochi is a tourist destination. And it attracts majorly French and Portuguese tourist due to the history of the place.
- The location had plenty of food joints & mostly provide local foods only without giving much options to tourist.
- Road side fruit shops don't look hygienic
- At Velno we are going to sell fresh fruits as well as fruit juices.
- Customers can pick their fruits and Velno staffs will squeeze/blend or slice it for them.
- There will be no e-commerce on the site (no buying of products through site)

Target Market(s)

Tourist & health conscious individuals who want to have fresh fruit or juice.

Coding

Coded - Design and coding required

Number of Pages Required

4 page

Font styles to use
Script

Colors

Designer to choose colors to be used in the design.

Requirements
Must have
• Back End. Editable website.
• Since it for fruits & juices, we will be selling fruits as per season or availability.
• Editable or back end will allow us to add or delete menus as per availability.
• The project much have 4 pages. Namely:
• - Home
• - Concept
• - Menu
• - Location & Contact
Nice to have
• Fresh feel of the website
Should not have
• E-commerce

```html
<!DOCTYPE html>
<html lang="en">
<head>
<meta charset="UTF-8">
<title>Velno – Fresh Fruit &amp; Juice</title>
<link href="https://fonts.googleapis.com/css2?family=Poppins:wght@400;500;600;700&family=Lato:wght@400;700&display=swap" rel="stylesheet">
<style>
:root{
  --green:#3a9a2c;
  --green-dark:#1f7f24;
  --frame:#138a2e;
  --orange:#ff6a0f;
  --orange-soft:#ff8a2a;
  --red:#e8452c;
  --ink:#2b2b2b;
  --text:#4a4a4a;
  --white:#ffffff;
}
*{margin:0;padding:0;box-sizing:border-box}
html,body{width:1200px;height:3741px;overflow:hidden;background:var(--white)}
body{position:relative;font-family:'Lato',sans-serif;color:var(--text)}
.abs{position:absolute}
.img-fill{position:absolute}

/* header */
.topbar{left:450px;top:0;width:750px;height:42px;background:var(--green);clip-path:polygon(0 0,100% 0,100% 100%,40px 100%)}
.topbar .phone{position:absolute;left:78px;top:9px;color:var(--white);font-size:17px;font-family:'Poppins',sans-serif;display:flex;align-items:center;gap:8px}
.topbar .social{position:absolute;left:272px;top:12px;display:flex;gap:32px}
.topbar .social span{width:16px;height:16px;border-radius:50%;background:var(--white);opacity:.9}
.logo{font-family:'Poppins',sans-serif;font-weight:700;color:var(--green-dark);font-size:68px;letter-spacing:1px;line-height:1}
.site-logo{left:128px;top:42px}
.nav{left:560px;top:70px;font-family:'Poppins',sans-serif;font-weight:600;font-size:18px;color:var(--ink)}
.nav a{color:inherit;text-decoration:none;position:absolute;white-space:nowrap}
.nav .active::after{content:"";position:absolute;left:-12px;right:-12px;top:36px;height:4px;background:var(--green-dark)}

/* hero */
.hero{left:0;top:138px;width:1200px;height:648px;clip-path:polygon(0 0,100% 0,100% 582px,0 100%);background:linear-gradient(110deg,#9aa58a 0%,#c9c6b5 40%,#e3d9cf 60%,#b9c49e 100%)}
.hero-title{left:139px;top:330px;width:520px;font-family:'Poppins',sans-serif;font-weight:600;font-size:33px;line-height:52px;color:var(--ink)}
.btn{display:flex;align-items:center;justify-content:center;font-family:'Poppins',sans-serif;font-weight:600;text-decoration:none}
.hero-btn{left:141px;top:506px;width:198px;height:64px;background:var(--green);color:var(--white);font-size:24px;border-radius:2px}
.arrow{width:50px;height:50px;border-radius:50%;background:var(--frame);display:flex;align-items:center;justify-content:center}
.arrow-out{width:52px;height:52px;border-radius:50%;border:2px solid var(--red);display:flex;align-items:center;justify-content:center;background:rgba(255,255,255,.7)}

/* about */
.frame{border:4px solid var(--frame)}
.about-title{left:577px;top:994px;font-family:'Poppins',sans-serif;font-weight:600;font-size:43px;color:#3d3d3d}
.about-text{left:577px;top:1070px;width:497px;font-size:14px;line-height:34.4px;text-align:justify;color:#4a4a4a}
.about-btn{left:581px;top:1342px;width:150px;height:50px;background:var(--orange);color:var(--white);font-size:20px;font-weight:500}

/* concept */
.concept{left:0;top:1482px;width:1200px;height:468px;background:linear-gradient(120deg,#ff7a1a 0%,#ff8f35 45%,#ff6d12 100%)}
.concept-title{left:0;top:1536px;width:1200px;text-align:center;font-family:'Poppins',sans-serif;font-weight:700;font-size:43px;color:var(--white)}
.concept-text{left:200px;top:1620px;width:800px;text-align:center;color:var(--white);font-size:14px;line-height:34.5px}
.concept-text strong{font-size:17px}
.concept-btn{left:510px;top:1832px;width:179px;height:54px;background:var(--white);color:var(--orange);font-size:20px}

/* menu */
.menu-title{left:0;top:2004px;width:1200px;text-align:center;font-family:'Poppins',sans-serif;font-weight:700;font-size:44px;color:var(--green-dark)}
.menu-text{left:260px;top:2092px;width:630px;text-align:center;font-size:13.5px;line-height:25px;color:#444}
.card{width:247px;height:317px;top:2201px;border:3px solid #d6d6d6;background:var(--white);box-shadow:0 1px 3px rgba(0,0,0,.15)}
.card h3{position:absolute;top:30px;width:100%;text-align:center;font-family:'Poppins',sans-serif;font-weight:600;font-size:21px;color:var(--red)}
.card .apple{position:absolute;left:113px;top:73px}
.card ul{list-style:none;position:absolute;left:40px;top:116px;width:170px}
.card li{display:flex;justify-content:space-between;font-family:'Poppins',sans-serif;font-size:16px;height:34px;line-height:34px}
.card li span:first-child{color:var(--orange-soft)}
.card li span:last-child{color:#333}

/* gallery */
.gallery{left:0;top:2665px;width:1200px;height:684px;background:linear-gradient(90deg,#f3ece4 0%,#faf6f1 50%,#f1ebe6 100%)}
.gallery-title{left:0;top:2722px;width:1200px;text-align:center;font-family:'Poppins',sans-serif;font-weight:600;font-size:44px;color:#3a3a3a}

/* footer */
.footer-logo{left:0;top:3432px;width:1200px;text-align:center}
.footer-nav{left:0;top:3540px;width:1200px;display:flex;justify-content:center;gap:20px;font-family:'Poppins',sans-serif;font-size:18px;color:var(--orange-soft)}
.footer-nav .sep{color:var(--orange)}
.footer-contact{left:0;top:3604px;width:1200px;display:flex;justify-content:center;align-items:center;gap:22px;font-family:'Poppins',sans-serif;color:#333}
.footer-contact .addr{font-size:14px;letter-spacing:1.5px}
.footer-contact .tel{font-size:18px}
.footer-contact .sep{color:var(--orange);font-size:22px}
.footer-contact .soc{width:20px;height:20px;background:#333;border-radius:3px}
.footer-rule{left:0;top:3671px;width:1200px;height:1px;background:var(--orange-soft)}
.copyright{left:112px;top:3692px;font-family:Arial,sans-serif;font-size:13px;color:#333}
</style>
</head>
<body>

<!-- header -->
<div class="abs topbar">
  <div class="phone">
    <svg width="16" height="16" viewBox="0 0 24 24"><path fill="#fff" d="M6.6 10.8a15 15 0 0 0 6.6 6.6l2.2-2.2c.3-.3.7-.4 1-.2 1.1.4 2.3.6 3.6.6.6 0 1 .4 1 1V20c0 .6-.4 1-1 1A17 17 0 0 1 3 4c0-.6.4-1 1-1h3.5c.6 0 1 .4 1 1 0 1.3.2 2.5.6 3.6.1.3 0 .7-.2 1z"/></svg>
    555-214-7730
  </div>
  <div class="social"><span></span><span></span><span></span><span></span><span></span></div>
</div>
<div class="abs logo site-logo">Velno</div>
<nav class="abs nav">
  <a class="active" style="left:0">Home</a>
  <a style="left:105px">Concept</a>
  <a style="left:233px">Menu</a>
  <a style="left:335px">About us</a>
  <a style="left:467px">Location</a>
</nav>

<!-- hero -->
<div class="abs hero" role="img" aria-label="Couple choosing fresh fruit at a market stall"></div>
<h1 class="abs hero-title">We make juice from the fresh fruits that you pick up yourself from the fruit basket.</h1>
<a class="abs btn hero-btn">Read More</a>
<div class="abs arrow" style="left:43px;top:401px"><svg width="22" height="22" viewBox="0 0 24 24"><path d="M20 12H5M11 5l-7 7 7 7" stroke="#fff" stroke-width="3" fill="none"/></svg></div>
<div class="abs arrow" style="left:1100px;top:401px"><svg width="22" height="22" viewBox="0 0 24 24"><path d="M4 12h15M13 5l7 7-7 7" stroke="#fff" stroke-width="3" fill="none"/></svg></div>

<!-- about -->
<div class="img-fill" style="left:828px;top:734px;width:372px;height:269px;border-radius:46% 40% 44% 50%;background:radial-gradient(circle at 40% 50%,#f3a03a,#d9473a 55%,#9cc043)" role="img" aria-label="Pile of fresh fruits: peach, orange, cherries and kiwi"></div>
<div class="abs frame" style="left:94px;top:970px;width:218px;height:373px"></div>
<div class="abs frame" style="left:17px;top:1068px;width:218px;height:330px"></div>
<div class="abs frame" style="left:266px;top:1068px;width:216px;height:327px"></div>
<div class="img-fill" style="left:99px;top:1024px;width:410px;height:273px;background:linear-gradient(100deg,#c4b658,#d99a4d 45%,#c4c2b8 75%,#d7b8a8)" role="img" aria-label="Vendor handing fruit to a customer at a fruit stand"></div>
<h2 class="abs about-title">About Us</h2>
<p class="abs about-text">As a health conscious customer, one has every right to know the fruit before she/he sips the first sip of juice made out of it.We at Velno insist our clientele to pick the fresh fruits themselves from our fruit baskets so they know what they are consuming. And we can blend or squeezed those fruits for them as per their wish i.e onlyfruit or fruit with some add-ons. And hence we don't sell juice by bottle size rather it is all the juice that we will get from the fruits that you pick up from our fruit basket.</p>
<a class="abs btn about-btn">Read More</a>
<div class="img-fill" style="left:1010px;top:1322px;width:174px;height:138px;border-radius:50%;background:radial-gradient(circle,#ffb23a,#f28a12 70%,rgba(242,138,18,0))" role="img" aria-label="Orange slice with juice splash"></div>

<!-- concept -->
<section class="abs concept" role="img" aria-label="Orange-toned background of sliced fruits"></section>
<h2 class="abs concept-title">Origin of the Concept</h2>
<p class="abs concept-text">Visit any fruit vendor and ask them what they do with the left over and if you are lucky enough you mayget the truth.<br><strong>“They sell their leftover to the juice bar”</strong><br>When you order a glass of juice from any place you may not have any idea about the condition of the<br>fruit before it was squeezed &amp;amp; served to you. Here is where we at Velno wanted to bring in<br>transparency.</p>
<a class="abs btn concept-btn">Read More</a>

<!-- menu -->
<div class="img-fill" style="left:0;top:1950px;width:244px;height:205px;border-radius:0 60% 50% 0;background:radial-gradient(circle at 40% 50%,#e9502f,#f6b42a 55%,rgba(246,180,42,0))" role="img" aria-label="Mango, pineapple and tropical fruits with splash"></div>
<h2 class="abs menu-title">Menu</h2>
<p class="abs menu-text">Lorem ipsum dolor sit amet, consectetur adipiscing elit, sed do eiusmod tempor incididunt ut labore et dolore magna aliqua. Quis ipsum suspendisse ultrices gravida. Risus commodo viverra maecenas ac-cumsan lacus vel facilisis.</p>
<div class="img-fill" style="left:937px;top:2075px;width:150px;height:137px;border-radius:50%;background:radial-gradient(circle,#e8413d,#c92d2d 55%,rgba(201,45,45,0))" role="img" aria-label="Watermelon slice with splash"></div>

<div class="abs card" style="left:193px">
  <h3>Product</h3>
  <svg class="apple" width="20" height="22" viewBox="0 0 20 22"><circle cx="10" cy="13" r="8" fill="#e8452c"/><path d="M10 5c1-3 4-4 5-3" stroke="#3a9a2c" stroke-width="2" fill="none"/></svg>
  <ul><li><span>Apple</span><span>3</span></li><li><span>Grapes</span><span>4</span></li><li><span>Orange</span><span>15</span></li><li><span>Mango</span><span>5</span></li><li><span>Blueberry</span><span>7</span></li></ul>
</div>
<div class="abs card" style="left:465px">
  <h3>Product</h3>
  <svg class="apple" width="20" height="22" viewBox="0 0 20 22"><circle cx="10" cy="13" r="8" fill="#e8452c"/><path d="M10 5c1-3 4-4 5-3" stroke="#3a9a2c" stroke-width="2" fill="none"/></svg>
  <ul><li><span>Apple</span><span>3</span></li><li><span>Grapes</span><span>4</span></li><li><span>Orange</span><span>15</span></li><li><span>Mango</span><span>5</span></li><li><span>Blueberry</span><span>7</span></li></ul>
</div>
<div class="abs card" style="left:734px">
  <h3>Product</h3>
  <svg class="apple" width="20" height="22" viewBox="0 0 20 22"><circle cx="10" cy="13" r="8" fill="#e8452c"/><path d="M10 5c1-3 4-4 5-3" stroke="#3a9a2c" stroke-width="2" fill="none"/></svg>
  <ul><li><span>Apple</span><span>3</span></li><li><span>Grapes</span><span>4</span></li><li><span>Orange</span><span>15</span></li><li><span>Mango</span><span>5</span></li><li><span>Blueberry</span><span>7</span></li></ul>
</div>
<div class="img-fill" style="left:276px;top:2484px;width:145px;height:138px;border-radius:50%;background:radial-gradient(circle,#a4cf45,#6fae2a 55%,rgba(111,174,42,0))" role="img" aria-label="Kiwi half with green splash"></div>
<div class="img-fill" style="left:988px;top:2455px;width:212px;height:206px;border-radius:60% 0 0 40%;background:radial-gradient(circle at 60% 45%,#c8263a,#e33a35 50%,rgba(227,58,53,0))" role="img" aria-label="Berries, kiwi and apple in red juice splash"></div>

<!-- gallery -->
<section class="abs gallery" role="img" aria-label="Faded background of a fruit market"></section>
<h2 class="abs gallery-title">Gallery</h2>
<div class="img-fill" style="left:113px;top:2847px;width:337px;height:424px;background:linear-gradient(160deg,#d9583a,#e6b238 45%,#c5332a 75%,#e7c340)" role="img" aria-label="Shopping cart full of lemons, apples and peppers"></div>
<div class="img-fill" style="left:461px;top:2847px;width:331px;height:208px;background:linear-gradient(120deg,#d48a3a,#cdbfa8 50%,#d9852f)" role="img" aria-label="Woman choosing fruit at a market"></div>
<div class="img-fill" style="left:461px;top:3065px;width:331px;height:206px;background:linear-gradient(120deg,#4f8a2e,#9cbc3a 40%,#e0b43a 65%,#c8362c)" role="img" aria-label="Vegetables and fruits on display"></div>
<div class="img-fill" style="left:800px;top:2847px;width:291px;height:424px;background:linear-gradient(180deg,#cfcac4,#c7463a 45%,#e89324 80%)" role="img" aria-label="Two women with a basket of oranges and pineapple"></div>
<div class="abs arrow-out" style="left:38px;top:3036px"><svg width="22" height="22" viewBox="0 0 24 24"><path d="M20 12H5M11 5l-7 7 7 7" stroke="#e8452c" stroke-width="2.5" fill="none"/></svg></div>
<div class="abs arrow-out" style="left:1112px;top:3036px"><svg width="22" height="22" viewBox="0 0 24 24"><path d="M4 12h15M13 5l7 7-7 7" stroke="#e8452c" stroke-width="2.5" fill="none"/></svg></div>

<!-- footer -->
<div class="abs logo footer-logo">Velno</div>
<nav class="abs footer-nav">
  <span>Home</span><span class="sep">/</span><span>Concept</span><span class="sep">/</span><span>Menu</span><span class="sep">/</span><span>About us</span><span class="sep">/</span><span>Location.</span>
</nav>
<div class="abs footer-contact">
  <svg width="16" height="20" viewBox="0 0 16 20"><path d="M8 0a7 7 0 0 0-7 7c0 5 7 13 7 13s7-8 7-13a7 7 0 0 0-7-7zm0 10a3 3 0 1 1 0-6 3 3 0 0 1 0 6z" fill="#333"/></svg>
  <span class="addr">Lorem ipsum dolor sit</span>
  <span class="sep">/</span>
  <svg width="20" height="20" viewBox="0 0 24 24"><path fill="#333" d="M6.6 10.8a15 15 0 0 0 6.6 6.6l2.2-2.2c.3-.3.7-.4 1-.2 1.1.4 2.3.6 3.6.6.6 0 1 .4 1 1V20c0 .6-.4 1-1 1A17 17 0 0 1 3 4c0-.6.4-1 1-1h3.5c.6 0 1 .4 1 1 0 1.3.2 2.5.6 3.6.1.3 0 .7-.2 1z"/></svg>
  <span class="tel">555-214-7730</span>
  <span class="sep">/</span>
  <span class="soc"></span><span class="soc"></span><span class="soc"></span><span class="soc"></span><span class="soc"></span>
</div>
<div class="abs footer-rule"></div>
<p class="abs copyright">© &nbsp;2019 All Right Reserved | Privacy Policy | Terms and Conditions</p>

</body>
</html>
```